Book cover design for the book titled "Quieter Under Lanterns."

create a book cover. The book title is, "Quieter Under Lanterns: A Ledger of Harbour Songs Across Mild Winters." The purpose of the book is to create awareness of how childhood trauma is impacting 7 out of 10 adults in the world today and that two-thirds of children will experience neglect and or abuse before their 18th birthday. One victim described that his mental and physical illness resulting from childhood trauma felt like he wa being pulled to the ground, that the force was "quieter under lanterns." The design should be clean and simple and communicate a crisis.

```html
<!DOCTYPE html>
<html lang="en">
<head>
<meta charset="UTF-8">
<title>Quieter Under Lanterns — Book Cover</title>
<link href="https://fonts.googleapis.com/css2?family=Bebas+Neue&family=Montserrat:wght@500&display=swap" rel="stylesheet">
<style>
  :root {
    --page: #ffffff;
    --cover-ink: #131418;
    --title: #ffffff;
    --author-band: #232937;
    --photo-wall: #9a9895;
    --photo-mid: #5a5957;
    --photo-shadow: #0e0f11;
  }
  html, body {
    margin: 0;
    width: 1200px;
    height: 1200px;
    overflow: hidden;
    background: var(--page);
  }
  .book-cover {
    position: absolute;
    left: 295px;
    top: 141px;
    width: 618px;
    height: 925px;
    display: block;
  }
  .title-word {
    font-family: "Bebas Neue", "Oswald", sans-serif;
    fill: var(--title);
  }
  .subtitle {
    font-family: "Montserrat", sans-serif;
    font-weight: 500;
    fill: var(--title);
    font-size: 27px;
    letter-spacing: 0.6px;
  }
  .author-name {
    font-family: "Bebas Neue", "Oswald", sans-serif;
    fill: var(--title);
    font-size: 33px;
    letter-spacing: 5px;
  }
  .rule { stroke: var(--title); stroke-width: 1.2; opacity: 0.9; }
</style>
</head>
<body>
<svg class="book-cover" viewBox="0 0 618 925" xmlns="http://www.w3.org/2000/svg">
  <defs>
    <linearGradient id="wall-tone" x1="0" y1="0" x2="1" y2="0">
      <stop offset="0" stop-color="var(--photo-shadow)"/>
      <stop offset="0.3" stop-color="#1c1c1e"/>
      <stop offset="0.6" stop-color="var(--photo-mid)"/>
      <stop offset="1" stop-color="var(--photo-wall)"/>
    </linearGradient>
    <radialGradient id="wall-light" cx="0.78" cy="0.18" r="0.55">
      <stop offset="0" stop-color="#b4b2ae" stop-opacity="0.55"/>
      <stop offset="1" stop-color="#b4b2ae" stop-opacity="0"/>
    </radialGradient>
    <radialGradient id="figure-glow" cx="0.5" cy="0.55" r="0.32">
      <stop offset="0" stop-color="#8c8a87" stop-opacity="0.55"/>
      <stop offset="0.6" stop-color="#3a3938" stop-opacity="0.35"/>
      <stop offset="1" stop-color="#3a3938" stop-opacity="0"/>
    </radialGradient>
    <radialGradient id="corner-shadow" cx="0" cy="0.4" r="0.6">
      <stop offset="0" stop-color="#0b0c0e" stop-opacity="0.9"/>
      <stop offset="1" stop-color="#0b0c0e" stop-opacity="0"/>
    </radialGradient>
    <linearGradient id="photo-fade" x1="0" y1="0" x2="0" y2="1">
      <stop offset="0" stop-color="#131418" stop-opacity="0"/>
      <stop offset="0.55" stop-color="#131418" stop-opacity="0.15"/>
      <stop offset="0.85" stop-color="#131418" stop-opacity="0.8"/>
      <stop offset="1" stop-color="#131418" stop-opacity="1"/>
    </linearGradient>
  </defs>

  <rect class="cover-ground" width="618" height="925" fill="var(--cover-ink)"/>

  <g class="cover-photo" role="img" aria-label="Black and white photograph of a distressed young child with clenched hands against a rough, dimly lit wall">
    <rect x="0" y="0" width="618" height="450" fill="url(#wall-tone)"/>
    <rect x="0" y="0" width="618" height="450" fill="url(#wall-light)"/>
    <rect x="0" y="0" width="618" height="450" fill="url(#figure-glow)"/>
    <rect x="0" y="0" width="618" height="450" fill="url(#corner-shadow)"/>
    <rect x="0" y="0" width="618" height="450" fill="url(#photo-fade)"/>
  </g>

  <text class="title-word" x="57" y="590" font-size="210" textLength="535" lengthAdjust="spacingAndGlyphs">QUIETER</text>

  <line class="rule" x1="59" y1="621" x2="264" y2="621"/>
  <text class="title-word" x="325" y="637" font-size="50" text-anchor="middle">UNDER</text>
  <line class="rule" x1="386" y1="621" x2="592" y2="621"/>

  <text class="title-word" x="57" y="800" font-size="210" textLength="535" lengthAdjust="spacingAndGlyphs">LANTERNS</text>

  <text class="subtitle" x="325" y="838" text-anchor="middle">A LEDGER OF HARBOUR SONGS</text>
  <text class="subtitle" x="325" y="876" text-anchor="middle">ACROSS MILD WINTERS</text>

  <rect class="author-band" x="0" y="887" width="618" height="38" fill="var(--author-band)"/>
  <text class="author-name" x="306" y="917" text-anchor="middle">AUTHOR NAME</text>
</svg>
</body>
</html>
```